website design for Company MVR

Our company name MVR(the grand mural limited), need design a website. It is a website that focuses on promoting art design in the world.
We will provide the existing logo design, the new website and logo should be matched to each other. The website has to include pages "Home" "Contact" "Service" and So on at least 6-8 pages. The site is mainly for publicity and promotion. We will have an existing domain and hosting.
Updates

We prefer the original design, thanks.

Target Market(s)

large public art

Industry/Entity Type

Architecture and design, large public art and sculpture manufacturer

Coding

Coded - Design and coding required

Number of Pages Required

5+ page

Requirements
Must have
• 1. the overall color has to match our logo color 2. Do not need to do any change on our logo including the color 3. Here is a similar style of the home page we like, it can be similar but must not same. Pls check the below link. https://www.velmardo.it/en-us/

```html
<!DOCTYPE html>
<html lang="en">
<head>
<meta charset="utf-8">
<title>MVR — The Grand Mural</title>
<link rel="stylesheet" href="https://fonts.googleapis.com/css2?family=Oswald:wght@400;500;600;700&family=Poppins:wght@400;500;600&display=swap">
<style>
:root{
  --ink:#111;
  --black:#000;
  --charcoal:#3b3b3b;
  --deep:#2a2a2a;
  --slate:#5e5e5e;
  --mist:#efefef;
  --line:#cfcfcf;
  --white:#fff;
  --muted:#6a6a6a;
  --head:'Oswald',sans-serif;
  --body:'Poppins',sans-serif;
}
*{margin:0;padding:0;box-sizing:border-box}
html,body{width:1200px;height:4121px;overflow:hidden;background:var(--white);font-family:var(--body);color:var(--ink)}
.page{position:relative;width:1200px;height:4121px;overflow:hidden}
.abs{position:absolute}
.photo{position:absolute}

/* header */
.site-header{position:absolute;left:0;top:0;width:1200px;height:86px;background:var(--white)}
.brand{position:absolute;left:88px;top:26px;font-family:var(--head);font-weight:500;font-size:30px;letter-spacing:2px;color:var(--charcoal);display:flex;align-items:center;gap:12px;white-space:nowrap}
.brand-mark{width:14px;height:14px;background:var(--charcoal)}
.main-nav{position:absolute;left:490px;top:34px;display:flex;gap:20px;font-family:var(--head);font-size:14px;color:var(--charcoal)}
.btn-contact{position:absolute;left:1002px;top:26px;width:108px;height:36px;background:var(--slate);color:var(--white);font-family:var(--head);font-size:14px;display:flex;align-items:center;justify-content:center}

/* hero */
.hero{position:absolute;left:0;top:86px;width:1200px;height:710px}
.hero-tag{position:absolute;left:104px;top:332px;font-family:var(--head);font-size:16px;color:var(--white)}
.hero-word{position:absolute;font-family:var(--head);font-weight:700;color:var(--white);line-height:1}
.slide-index{position:absolute;left:1140px;top:190px;width:2px;height:150px;background:#555}
.slide-index::after{content:"";position:absolute;left:0;top:50px;width:2px;height:40px;background:var(--white)}
.slide-num{position:absolute;left:1156px;font-family:var(--head);font-size:13px;color:#999}
.scroll-btn{position:absolute;left:997px;top:571px;width:112px;height:112px;border-radius:50%;background:var(--white);box-shadow:0 8px 24px rgba(0,0,0,.18);display:flex;align-items:center;justify-content:center}

/* about */
.eyebrow{font-family:var(--body);font-weight:600;font-size:11px;letter-spacing:.5px;color:var(--ink)}
.about-rule{position:absolute;left:178px;top:858px;width:1px;height:102px;background:var(--ink)}
.about-copy{position:absolute;left:147px;top:976px;width:430px}
.about-copy h2{font-family:var(--head);font-weight:600;font-size:46px;line-height:1.1;margin-top:10px}
.about-copy .sub{font-size:13px;font-weight:500;margin-top:6px}
.about-copy p.text{font-size:13.5px;line-height:24px;color:#444;margin-top:28px}
.btn-more{display:inline-block;margin-top:30px;width:118px;height:33px;line-height:33px;text-align:center;background:var(--slate);color:var(--white);font-size:11px;font-weight:600}
.frame{position:absolute;left:699px;top:973px;width:354px;height:376px;border:19px solid var(--slate)}

/* section titles */
.section-title{position:absolute;left:0;width:1200px;text-align:center}
.section-title h2{font-family:var(--head);font-weight:600;font-size:44px;line-height:1.1;margin-top:6px}
.section-title .tick{width:44px;height:1px;background:#bbb;margin:10px auto 0}

/* services */
.svc-band{position:absolute;left:0;top:1776px;width:600px;height:341px;background:var(--mist)}
.card{position:absolute;top:1562px;width:331px;height:408px;background:var(--white);box-shadow:0 10px 30px rgba(0,0,0,.08)}
.card .photo{left:0;top:0;width:331px;height:214px}
.card h3{position:absolute;left:30px;top:242px;font-family:var(--head);font-weight:600;font-size:20px}
.card p{position:absolute;left:30px;top:278px;width:275px;font-size:12.5px;line-height:21px;color:#555}
.card .explore{position:absolute;left:30px;top:354px;font-size:14px;font-weight:600;color:var(--muted);text-decoration:underline;display:flex;gap:10px;align-items:center}
.pager{position:absolute;top:2018px;width:50px;height:50px;border:1.5px solid var(--ink);display:flex;align-items:center;justify-content:center}
.pager-track{position:absolute;left:142px;top:2043px;width:314px;height:1px;background:#bdbdbd}

/* award */
.award-title{position:absolute;left:0;width:1200px;text-align:center;font-family:var(--head);font-weight:600;color:var(--white);line-height:1}
.play-btn{position:absolute;left:88px;top:2594px;width:112px;height:112px;border-radius:50%;background:var(--white);box-shadow:0 8px 24px rgba(0,0,0,.2);display:flex;align-items:center;justify-content:center}

/* blog */
.post{position:absolute;top:3181px;width:314px;height:166px;background:var(--white);box-shadow:0 10px 30px rgba(0,0,0,.1);padding:32px 34px}
.post .meta{font-size:11px;color:#444}
.post h3{font-family:var(--head);font-weight:500;font-size:18px;line-height:24px;margin-top:8px}
.post p{font-size:12.5px;line-height:20px;color:#666;margin-top:6px}

/* gallery strip */
.strip{position:absolute;top:3466px;width:200px;height:200px}

/* footer */
.site-footer{position:absolute;left:0;top:3666px;width:1200px;height:455px;background:var(--charcoal)}
.footer-brand{position:absolute;left:0;width:1200px;top:120px;text-align:center;font-family:var(--head);font-weight:500;font-size:34px;letter-spacing:2px;color:var(--white)}
.footer-nav{position:absolute;left:0;width:1200px;top:198px;display:flex;justify-content:center;gap:22px;font-family:var(--head);font-size:14px;color:var(--white)}
.socials{position:absolute;left:0;width:1200px;top:254px;display:flex;justify-content:center;gap:10px}
.socials span{width:29px;height:29px;border-radius:50%;background:#555;display:block}
.chat-btn{position:absolute;left:1079px;top:183px;width:52px;height:52px;border-radius:50%;background:var(--white)}
.copyright{position:absolute;left:0;top:406px;width:1200px;height:49px;background:var(--deep);color:#ddd;font-size:11px;font-weight:500;text-align:center;line-height:49px}
</style>
</head>
<body>
<div class="page">

  <header class="site-header">
    <div class="brand"><span class="brand-mark"></span>MVR THE GRAND MURAL</div>
    <nav class="main-nav"><span>HOME</span><span>ABOUT US</span><span>OUR SERVICES</span><span>PROJECTS</span><span>FINE ART</span><span>MEMBERSHIP</span><span>ARTISTS</span></nav>
    <div class="btn-contact">CONTACT US</div>
  </header>

  <section class="hero">
    <svg class="abs" style="left:0;top:0" width="1200" height="710" viewBox="0 86 1200 710">
      <rect x="0" y="86" width="1200" height="710" fill="#000"/>
      <polygon points="624,86 952,86 600,728 300,740" fill="#1c1c1c"/>
      <polygon points="352,728 1200,597 1200,640 0,766" fill="#bdbdbd"/>
      <polygon points="0,766 1200,640 1200,796 0,796" fill="#fff"/>
    </svg>
    <div class="photo" role="img" aria-label="Marble baroque sculpture of a winged figure" style="left:272px;top:34px;width:640px;height:584px;background:radial-gradient(ellipse at 50% 45%,#bcbcbc 0%,#6f6f6f 40%,rgba(40,40,40,0) 70%)"></div>
    <div class="hero-word" style="left:806px;top:96px;font-size:128px">TURE</div>
    <div class="hero-tag">MVR THE GRAND MURAL</div>
    <div class="hero-word" style="left:102px;top:360px;font-size:128px">SCULP</div>
    <div class="slide-index"></div>
    <div class="slide-num" style="top:190px">01</div>
    <div class="slide-num" style="top:248px;color:#fff">02</div>
    <div class="slide-num" style="top:308px">03</div>
    <div class="scroll-btn">
      <svg width="24" height="52" viewBox="0 0 24 52"><polygon points="2,2 22,2 12,18" fill="#555"/><polygon points="2,20 22,20 12,36" fill="#555"/><polygon points="4,38 20,38 12,50" fill="none" stroke="#555" stroke-width="2"/></svg>
    </div>
  </section>

  <section class="about">
    <div class="about-rule"></div>
    <div class="about-copy">
      <div class="eyebrow">ABOUT US</div>
      <h2>THE GRAND MURAL</h2>
      <div class="sub">ART IS EMOTION. ART INSPIRES. ART IS ORIGINAL</div>
      <p class="text">Aenean sollicitudin, lorem quis bibendum auctor, nisi elit consequat ipsum, nec sagittis sem nibh id elit duis sed odio amet nibh vulputate cursus amet mauris morbi accumsan ipsum velit. Nam nec tellus a odio tincidunt...</p>
      <span class="btn-more">LEARN MORE</span>
    </div>
    <div class="frame"></div>
    <div class="photo" role="img" aria-label="Skyscraper seen from below in black and white" style="left:683px;top:752px;width:287px;height:445px;background:linear-gradient(160deg,#9a9a9a,#3a3a3a 45%,#111)"></div>
    <div class="photo" role="img" aria-label="Visitor viewing framed portraits in a dark gallery" style="left:616px;top:994px;width:200px;height:283px;background:linear-gradient(180deg,#4a4a4a,#1a1a1a);border:4px solid #fff;box-shadow:0 10px 30px rgba(0,0,0,.25)"></div>
  </section>

  <section class="services">
    <div class="section-title" style="top:1446px"><div class="eyebrow">SERVICES</div><h2>WE SPECIALIZE IN</h2><div class="tick"></div></div>
    <div class="svc-band"></div>
    <article class="card" style="left:88px">
      <div class="photo" role="img" aria-label="Curved modern building facade with orange balconies" style="background:linear-gradient(135deg,#2c6d78,#c4623a 55%,#3a2a22)"></div>
      <h3>ARCHITECTURE AND DESIGN</h3>
      <p>Aenean sollicitudin, lorem quis auctor, nisi elit consequat ipsum, nec sagittis sem nibh id elit duis sed odio...</p>
      <span class="explore">Explore <svg width="14" height="10" viewBox="0 0 14 10"><path d="M0 5h12M8 1l4 4-4 4" fill="none" stroke="#6a6a6a" stroke-width="1.3"/></svg></span>
    </article>
    <article class="card" style="left:434px">
      <div class="photo" role="img" aria-label="Stacked bronze animal sculpture in a city plaza" style="background:linear-gradient(180deg,#5d7fa8,#5a5a5a 55%,#2e2e2e)"></div>
      <h3>LARGE PUBLIC ART</h3>
      <p>Aenean sollicitudin, lorem quis auctor, nisi elit consequat ipsum, nec sagittis sem nibh id elit duis sed odio...</p>
      <span class="explore">Explore <svg width="14" height="10" viewBox="0 0 14 10"><path d="M0 5h12M8 1l4 4-4 4" fill="none" stroke="#6a6a6a" stroke-width="1.3"/></svg></span>
    </article>
    <article class="card" style="left:778px">
      <div class="photo" role="img" aria-label="White marble classical bust" style="background:radial-gradient(ellipse at 45% 45%,#e8e4de 0%,#8a7e70 45%,#3b3128)"></div>
      <h3>SCULPTURE MANUFACTURER</h3>
      <p>Aenean sollicitudin, lorem quis auctor, nisi elit consequat ipsum, nec sagittis sem nibh id elit duis sed odio...</p>
      <span class="explore">Explore <svg width="14" height="10" viewBox="0 0 14 10"><path d="M0 5h12M8 1l4 4-4 4" fill="none" stroke="#6a6a6a" stroke-width="1.3"/></svg></span>
    </article>
    <div class="pager" style="left:70px"><svg width="20" height="12" viewBox="0 0 20 12"><path d="M20 6H2M6 1L1 6l5 5" fill="none" stroke="#111" stroke-width="1.4"/></svg></div>
    <div class="pager-track"></div>
    <div class="pager" style="left:477px"><svg width="20" height="12" viewBox="0 0 20 12"><path d="M0 6h18M14 1l5 5-5 5" fill="none" stroke="#111" stroke-width="1.4"/></svg></div>
  </section>

  <section class="award">
    <div class="photo" role="img" aria-label="Dark gallery hall with framed photographs on the walls" style="left:0;top:2117px;width:1200px;height:680px;background:linear-gradient(180deg,#3a3a3a 0%,#262626 45%,#141414 100%)"></div>
    <svg class="abs" style="left:0;top:2600px" width="1200" height="200" viewBox="0 2600 1200 200">
      <polygon points="0,2624 1200,2752 1200,2795 0,2652" fill="#bdbdbd"/>
      <polygon points="0,2652 1200,2795 1200,2800 0,2800" fill="#fff"/>
    </svg>
    <div class="award-title" style="top:2355px;font-size:56px">A DESIGN AWARD AND</div>
    <div class="award-title" style="top:2412px;font-size:108px;font-weight:700">COMPETITION</div>
    <div class="play-btn"><svg width="22" height="26" viewBox="0 0 22 26"><polygon points="2,1 21,13 2,25" fill="#555"/></svg></div>
  </section>

  <section class="blog">
    <div class="section-title" style="top:2826px"><div class="eyebrow">ARTICLE</div><h2>LATEST BLOG</h2></div>
    <div class="photo" role="img" aria-label="Museum room with framed paintings and rope barriers" style="left:171px;top:2938px;width:408px;height:241px;background:linear-gradient(90deg,#3c4046 0%,#3c4046 31%,#8b9aa8 32%,#c4ccd3)"></div>
    <div class="photo" style="left:171px;top:3179px;width:127px;height:93px;background:#34383d"></div>
    <article class="post" style="left:266px">
      <div class="meta">byElena &nbsp;•&nbsp; January 2021</div>
      <h3>SOME BLOG HEADING GOES HERE CITY NAME COUNTRY</h3>
      <p>Aenean sollicitudin, lorem quis nec sagittis sem nibh id elit duis sed...</p>
    </article>
    <div class="photo" role="img" aria-label="Visitors viewing old master paintings in a gallery" style="left:613px;top:2938px;width:414px;height:241px;background:linear-gradient(135deg,#5a3a22,#2a1e18 60%,#1c1612)"></div>
    <div class="photo" style="left:613px;top:3179px;width:102px;height:93px;background:#231a15"></div>
    <article class="post" style="left:715px">
      <div class="meta">byElena &nbsp;•&nbsp; January 2021</div>
      <h3>SOME BLOG HEADING GOES HERE CITY NAME COUNTRY</h3>
      <p>Aenean sollicitudin, lorem quis nec sagittis sem nibh id elit duis sed...</p>
    </article>
  </section>

  <section class="gallery-strip">
    <div class="strip" role="img" aria-label="Long gallery corridor with lit artworks" style="left:0;background:linear-gradient(180deg,#2a2a2a,#6a5a58)"></div>
    <div class="strip" role="img" aria-label="Painter working at an easel" style="left:200px;background:linear-gradient(135deg,#6b7f94,#a77a4e)"></div>
    <div class="strip" role="img" aria-label="White spiral staircase" style="left:400px;background:linear-gradient(135deg,#5a5a5a,#d8d8d8)"></div>
    <div class="strip" role="img" aria-label="Gilded statue in a warm lit niche" style="left:600px;background:radial-gradient(ellipse at 50% 50%,#c48a4a,#3a2412)"></div>
    <div class="strip" role="img" aria-label="Silhouetted visitor in a bright gallery" style="left:800px;background:linear-gradient(180deg,#d4d4d4,#7a7a7a)"></div>
    <div class="strip" role="img" aria-label="Classical bust with a floral crown" style="left:1000px;background:radial-gradient(ellipse at 50% 55%,#c8c0b8,#3a3a40)"></div>
  </section>

  <footer class="site-footer">
    <div class="footer-brand">MVR THE GRAND MURAL</div>
    <nav class="footer-nav"><span>HOME</span><span>ABOUT US</span><span>OUR SERVICES</span><span>PROJECTS</span><span>FINE ART</span><span>MEMBERSHIP</span><span>ARTISTS</span><span>CONTACT US</span></nav>
    <div class="socials"><span></span><span></span><span></span><span></span></div>
    <div class="chat-btn"></div>
    <div class="copyright">© COPYRIGHT 2021 THE GRAND MURAL ALL RIGHTS RESERVED</div>
  </footer>

</div>
</body>
</html>
```